Business card to promote business guidance

I need a card design to give to all my customers advertising a way to build a business exactly like the one they just bought from. I have an online store and will include one with each shipment. It should state the way to financial freedom and working for yourself

Target Market(s)

Young Entrepreneurs that want to start and don't know how

Industry/Entity Type

Business

Contact Information for Business Card

"You just bought from a successful company on Vorpex. I have a unique business model, discovered by me, unlike any other that can make anyone successful. Follow me and message me for exactly the same model. If you ever wanted to work for yourself, I will teach you how. It's not a pipe dream, allow me to guide you out of the box."

Colors
85abd2

Requirements
Must have
• website www.loganmerewick.com
instagram @theloganmerewick

```html
<!DOCTYPE html>
<html lang="en">
<head>
<meta charset="utf-8">
<title>Business Card – Contact Information</title>
<link rel="stylesheet" href="https://fonts.googleapis.com/css2?family=Bungee&family=Montserrat:ital,wght@0,400;0,500;1,400&display=swap">
<style>
  :root {
    --navy: #1f396a;
    --sky: #85abd2;
    --white: #ffffff;
    --page: #ffffff;
  }
  * { margin: 0; padding: 0; box-sizing: border-box; }
  html, body {
    width: 1027px;
    height: 1200px;
    overflow: hidden;
    background: var(--page);
  }
  .card {
    position: absolute;
    left: 49px;
    top: 321px;
    width: 929px;
    height: 557px;
    background: var(--sky);
    overflow: hidden;
  }
  .card__top {
    position: absolute;
    left: 0; top: 0;
    width: 100%;
    height: 305px;
    background: var(--navy);
  }
  .card__rule {
    position: absolute;
    left: 0; top: 305px;
    width: 100%;
    height: 2px;
    background: var(--sky);
  }
  .card__band {
    position: absolute;
    left: 0; top: 307px;
    width: 100%;
    height: 11px;
    background: var(--navy);
  }
  .heading {
    position: absolute;
    top: 78px;
    left: 0;
    width: 100%;
    text-align: center;
    font-family: "Bungee", sans-serif;
    font-size: 15px;
    letter-spacing: 1px;
    color: var(--white);
  }
  .heading__dots {
    position: absolute;
    top: 103px;
    left: 50%;
    transform: translateX(-50%);
  }
  .message {
    position: absolute;
    top: 124px;
    left: 66px;
    width: 797px;
    font-family: "Montserrat", sans-serif;
    font-style: italic;
    font-size: 16.5px;
    line-height: 28.7px;
    letter-spacing: 0.6px;
    text-align: justify;
    color: var(--white);
  }
  .contacts {
    position: absolute;
    top: 362px;
    left: 244px;
    list-style: none;
  }
  .contacts__item {
    display: flex;
    align-items: center;
    height: 34px;
    margin-bottom: 24px;
    font-family: "Montserrat", sans-serif;
    font-weight: 500;
    font-size: 24px;
    letter-spacing: 1.2px;
    color: var(--navy);
  }
  .contacts__mark {
    width: 28px;
    height: 28px;
    margin-right: 16px;
    background: var(--navy);
    flex: none;
  }
</style>
</head>
<body>
  <section class="card" aria-label="Business card, contact information side">
    <div class="card__top"></div>
    <div class="card__rule"></div>
    <div class="card__band"></div>

    <h1 class="heading">Contact Information</h1>
    <svg class="heading__dots" width="184" height="6" viewBox="0 0 184 6" aria-hidden="true">
      <g fill="#85abd2">
        <circle cx="3" cy="3" r="2"/><circle cx="14.8" cy="3" r="2"/><circle cx="26.6" cy="3" r="2"/>
        <circle cx="38.4" cy="3" r="2"/><circle cx="50.2" cy="3" r="2"/><circle cx="62" cy="3" r="2"/>
        <circle cx="73.8" cy="3" r="2"/><circle cx="85.6" cy="3" r="2"/><circle cx="97.4" cy="3" r="2"/>
        <circle cx="109.2" cy="3" r="2"/><circle cx="121" cy="3" r="2"/><circle cx="132.8" cy="3" r="2"/>
        <circle cx="144.6" cy="3" r="2"/><circle cx="156.4" cy="3" r="2"/><circle cx="168.2" cy="3" r="2"/>
        <circle cx="180" cy="3" r="2"/>
      </g>
    </svg>

    <p class="message">"You just bought from a successful company on Vorpex. I have a unique business model, discovered by me, unlike any other that can make anyone successful. Follow me and message me for exactly the same model. If you ever wanted to work for yourself, I will teach you how. It's not a pipe dream, allow me to guide you out of the box."</p>

    <ul class="contacts">
      <li class="contacts__item"><span class="contacts__mark" aria-hidden="true"></span>website www.loganmerewick.com</li>
      <li class="contacts__item"><span class="contacts__mark" aria-hidden="true"></span>instagram @theloganmerewick</li>
    </ul>
  </section>
</body>
</html>
```